Velmora Fitness business cards

I need a business card for my company called Velmora Fitness. I am a certified personal trainer, QLM certified, Pivot Plié certified, and Vigor Tracks certified. I am also an independent KORVEL rep, the number #1 rated nutritional and supplement product in the country. The card needs to convey Health, Wellness, Living Life and Loving It. I want it to be clean, sharp, eye-catching. Tantalizing.
Updates

for some reason, I'm unable to upload the pics I need. Stay tuned..

Industry/Entity Type

Business

Contact Information for Business Card

Velmora Fitness
Tova Lindqvam, Owner
tova@velmorafitness.example
555-372-4819
velmorafitness.example
tova@velmorafitness.example

Font styles to use
Serif

Requirements
Must have
• Must use pic of me and KORVEL logo

```html
<!DOCTYPE html>
<html lang="en">
<head>
<meta charset="utf-8">
<title>Velmora Fitness — Business Cards</title>
<link rel="stylesheet" href="https://fonts.googleapis.com/css2?family=Oswald:wght@500;600;700&family=Open+Sans:wght@300;400&display=swap">
<style>
  :root {
    --page-bg: #e4e3e6;
    --card-black: #1e1e1e;
    --brand-yellow: #f5d81c;
    --photo-light: #c9d2d6;
    --photo-mid: #a9b4b8;
    --photo-warm: #b89a80;
    --badge-blue: #2b6cb0;
    --text-light: #ffffff;
  }
  * { margin: 0; padding: 0; box-sizing: border-box; }
  html, body {
    width: 1200px; height: 900px; overflow: hidden;
    background: var(--page-bg);
  }
  .sheet {
    position: relative; width: 1200px; height: 900px;
  }
  .card {
    position: absolute; top: 302px;
    width: 520px; height: 297px;
    background: var(--card-black);
    overflow: hidden;
    box-shadow: 0 6px 14px rgba(0,0,0,0.35);
  }
  .card--front { left: 60px; }
  .card--back { left: 620px; }

  /* Front: wordmark with stripes */
  .wordmark {
    position: absolute;
    font-family: 'Oswald', 'Arial Narrow', sans-serif;
    font-weight: 600;
    color: var(--brand-yellow);
    line-height: 1;
    letter-spacing: -0.5px;
  }
  .wordmark__top { left: 66px; top: 60px; font-size: 56px; }
  .wordmark__bottom { left: 152px; top: 136px; font-size: 80px; }
  .stripes { position: absolute; left: 0; top: 113px; width: 520px; height: 34px; }

  /* Back: photo + contact */
  .portrait {
    position: absolute; left: 0; top: 0;
    width: 230px; height: 297px;
    background:
      radial-gradient(ellipse 45% 60% at 50% 55%, var(--photo-warm) 0%, rgba(184,154,128,0) 70%),
      linear-gradient(180deg, var(--photo-light), var(--photo-mid));
  }
  .contact {
    position: absolute; left: 276px; top: 50px;
    color: var(--brand-yellow);
  }
  .contact__first {
    font-family: 'Oswald', 'Arial Narrow', sans-serif;
    font-weight: 700; font-size: 96px; line-height: 0.9;
    letter-spacing: -1px;
  }
  .contact__last {
    font-family: 'Oswald', 'Arial Narrow', sans-serif;
    font-weight: 700; font-size: 24px; line-height: 1;
    text-transform: uppercase; margin-top: 4px;
  }
  .contact__role {
    font-family: 'Open Sans', Arial, sans-serif;
    font-weight: 400; font-size: 12px; margin-top: 2px;
  }
  .contact__phone {
    font-family: 'Open Sans', Arial, sans-serif;
    font-weight: 300; font-size: 21px; margin-top: 4px;
  }
  .contact__line {
    font-family: 'Open Sans', Arial, sans-serif;
    font-weight: 300; font-size: 13.5px; line-height: 1.3;
  }
  .partner {
    position: absolute; right: 14px; bottom: 26px;
    display: flex; flex-direction: column; align-items: center; gap: 4px;
  }
  .partner__dot {
    width: 40px; height: 40px; border-radius: 50%;
    background: var(--badge-blue);
  }
  .partner__name {
    font-family: 'Oswald', 'Arial Narrow', sans-serif;
    font-weight: 500; font-size: 12px; letter-spacing: 0.5px;
    color: var(--text-light);
  }
</style>
</head>
<body>
<main class="sheet">
  <section class="card card--front" aria-label="Card front">
    <svg class="stripes" viewBox="0 0 520 34" aria-hidden="true">
      <rect x="0" y="0" width="520" height="13" fill="var(--brand-yellow)"/>
      <rect x="0" y="19" width="520" height="3" fill="var(--brand-yellow)"/>
      <rect x="0" y="28" width="520" height="3" fill="var(--brand-yellow)"/>
    </svg>
    <span class="wordmark wordmark__top">Velmora</span>
    <span class="wordmark wordmark__bottom">Fitness</span>
  </section>

  <section class="card card--back" aria-label="Card back">
    <div class="portrait" role="img" aria-label="Photo of the trainer in workout wear, leaning forward with hands on knees"></div>
    <div class="contact">
      <div class="contact__first">TOVA</div>
      <div class="contact__last">Lindqvam</div>
      <div class="contact__role">Owner</div>
      <div class="contact__phone">555-372-4819</div>
      <div class="contact__line">tova@velmorafitness.example</div>
      <div class="contact__line">www.velmorafitness.example</div>
    </div>
    <div class="partner">
      <span class="partner__dot" aria-hidden="true"></span>
      <span class="partner__name">KORVEL</span>
    </div>
  </section>
</main>
</body>
</html>
```